Power Washing Business Easy Postcard Design

We need a postcard designed for our company, which does residential power washing. We clean houses, decks, driveways and fences. The design should be understated, high end with minimalist graphics. No bubbles or wild colors. The name of the business is "tallpine power washing" which should be rendered all lower case in a san serif font. Sample files in blue or white are attached. The attached files aren't our logo, just a model. The font doesn't have to be exact and "power washing" needs to be added to it.The postcard size is the Parcel Inkly 8.64" X 5.59". The photo which is attached should fill the whole front of the card.

The text elements on the front are:
1) "tallpine power washing"- as per the attached files, can be broken into two lines

2) "Mention this card and receive a FREE standard size Deck Wash"

3) "804-317-5286"

4) "tallpinepowerwashing.com" (this font size can be smaller than the phone number.)

5)"We Clean:- Houses- Decks- Driveways- Fences"The arrangement is the text is up to you. The text should not overpower the image.

Target Market(s)

Homeowners

Industry/Entity Type

Residential

Font styles to use
Sans Serif

Requirements
Should not have
• Garish graphics

```html
<!DOCTYPE html>
<html lang="en">
<head>
<meta charset="utf-8">
<title>tallpine power washing – postcard</title>
<link href="https://fonts.googleapis.com/css2?family=Roboto:wght@300;400;700&display=swap" rel="stylesheet">
<style>
  :root {
    --stage: #3c3c3e;
    --card-back: #e8f2f9;
    --navy: #2f4a7e;
    --grey: #707476;
    --ink: #1f1f1f;
    --rule: #8f9aa3;
    --green: #8cc043;
    --orange: #f39a2b;
    --purple: #8c6aae;
    --cyan: #27b5df;
    --white: #ffffff;
    --offer-band: rgba(31, 45, 80, 0.55);
  }
  * { box-sizing: border-box; margin: 0; padding: 0; }
  html, body { width: 1200px; height: 873px; overflow: hidden; }
  body {
    background: var(--stage);
    font-family: "Roboto", Arial, sans-serif;
    position: relative;
  }
  .postcard {
    position: absolute;
    left: 290px;
    width: 620px;
    height: 401px;
    overflow: hidden;
  }
  .postcard--back { top: 20px; background: var(--card-back); }
  .postcard--front { top: 452px; }

  .brand { position: absolute; line-height: 1; }
  .brand__name { display: block; font-weight: 400; color: var(--navy); letter-spacing: -0.5px; }
  .brand__sub { display: block; font-weight: 300; color: var(--grey); }

  .services { position: absolute; }
  .services__title { font-size: 17px; color: var(--ink); font-weight: 400; margin-bottom: 5px; }
  .services__list { display: flex; gap: 5px; list-style: none; }
  .tile {
    width: 66px; height: 46px;
    display: flex; flex-direction: column; align-items: center; justify-content: flex-end;
    color: var(--white); font-size: 10.5px; padding-bottom: 3px;
  }
  .tile svg { width: 28px; height: 22px; margin-bottom: 2px; }
  .tile--houses { background: var(--green); }
  .tile--decks { background: var(--orange); }
  .tile--driveways { background: var(--purple); }
  .tile--fences { background: var(--cyan); }

  .contact { position: absolute; line-height: 1; }
  .contact__phone { display: flex; align-items: center; gap: 6px; font-weight: 700; }
  .contact__web { display: block; font-weight: 400; }

  /* back */
  .postcard--back .brand { left: 62px; top: 34px; }
  .postcard--back .brand__name { font-size: 40px; }
  .postcard--back .brand__sub { font-size: 22px; margin-top: -2px; }
  .postcard--back .services { left: 40px; top: 132px; }
  .postcard--back .services__title { margin-left: 88px; }
  .worker-photo {
    position: absolute; left: 60px; top: 218px; width: 230px; height: 92px;
    background: radial-gradient(ellipse at 55% 40%, #c9d7e4 0%, #e3edf5 70%, var(--card-back) 100%);
  }
  .postcard--back .contact { left: 42px; top: 316px; color: var(--ink); }
  .postcard--back .contact__phone { font-size: 31px; }
  .postcard--back .contact__phone svg { width: 26px; height: 26px; }
  .postcard--back .contact__web { font-size: 19px; margin-top: 4px; }
  .divider { position: absolute; left: 322px; top: 34px; width: 1px; height: 320px; background: var(--rule); }
  .address-line { position: absolute; left: 372px; width: 212px; height: 1px; background: var(--rule); }

  /* front */
  .house-photo {
    position: absolute; inset: 0;
    background: linear-gradient(180deg, #8fa6d8 0%, #b9c6e6 22%, #d9cfc0 42%, #a99a86 62%, #6f8a4d 80%, #4f8a2e 100%);
  }
  .postcard--front .brand { left: 30px; top: 80px; }
  .postcard--front .brand__name { font-size: 36px; color: var(--navy); }
  .postcard--front .brand__sub { font-size: 21px; color: var(--white); margin-left: 18px; margin-top: -2px; }
  .postcard--front .services { right: 24px; top: 32px; }
  .postcard--front .services__title { color: var(--white); margin-left: 14px; }
  .offer {
    position: absolute; left: 24px; top: 326px; width: 200px;
    padding: 7px 10px;
    background: var(--offer-band);
    color: var(--white);
    font-size: 13px; line-height: 1.3; font-weight: 400;
  }
  .offer__free { font-weight: 700; }
  .postcard--front .contact { right: 34px; top: 316px; color: var(--white); }
  .postcard--front .contact__phone { font-size: 40px; }
  .postcard--front .contact__phone svg { width: 32px; height: 32px; }
  .postcard--front .contact__web { font-size: 21px; margin-top: 4px; margin-left: 28px; }
</style>
</head>
<body>

<svg width="0" height="0" style="position:absolute" aria-hidden="true">
  <defs>
    <symbol id="icon-phone" viewBox="0 0 32 32">
      <circle cx="16" cy="16" r="14" fill="none" stroke="currentColor" stroke-width="2.5"/>
      <path d="M11 9c1-1 2-1 2.5 0l1.5 3c.4.8 0 1.5-.6 2l-1 .8c.8 2 2.3 3.5 4.3 4.3l.8-1c.5-.6 1.2-1 2-.6l3 1.5c1 .5 1 1.5 0 2.5-1.5 1.5-3.5 1.8-6 .5-3-1.6-5.2-3.8-6.8-6.8-1.3-2.5-1-4.5.3-6.2z" fill="currentColor"/>
    </symbol>
    <symbol id="icon-house" viewBox="0 0 28 22">
      <path d="M2 11 14 3l12 8M5 9.5V20h18V9.5M11 20v-6h6v6" fill="none" stroke="#fff" stroke-width="1.5"/>
    </symbol>
    <symbol id="icon-deck" viewBox="0 0 28 22">
      <path d="M4 8a10 6 0 0 1 20 0zM14 8v12M6 20h16M7 14h5v6M16 14h5v6" fill="none" stroke="#fff" stroke-width="1.5"/>
    </symbol>
    <symbol id="icon-car" viewBox="0 0 28 22">
      <path d="M3 6 14 1l11 5v15M3 6v15M7 18v-5l2-4h10l2 4v5zM9 18v2M19 18v2" fill="none" stroke="#fff" stroke-width="1.5"/>
    </symbol>
    <symbol id="icon-fence" viewBox="0 0 28 22">
      <path d="M4 20V5l2-2 2 2v15M12 20V5l2-2 2 2v15M20 20V5l2-2 2 2v15M2 9h24M2 15h24" fill="none" stroke="#fff" stroke-width="1.5"/>
    </symbol>
  </defs>
</svg>

<section class="postcard postcard--back">
  <div class="brand">
    <span class="brand__name">tallpine</span>
    <span class="brand__sub">power washing</span>
  </div>

  <div class="services">
    <p class="services__title">We Clean:-</p>
    <ul class="services__list">
      <li class="tile tile--houses"><svg><use href="#icon-house"/></svg>Houses</li>
      <li class="tile tile--decks"><svg><use href="#icon-deck"/></svg>Decks</li>
      <li class="tile tile--driveways"><svg><use href="#icon-car"/></svg>Driveways</li>
      <li class="tile tile--fences"><svg><use href="#icon-fence"/></svg>Fences</li>
    </ul>
  </div>

  <div class="worker-photo" role="img" aria-label="Photo of a smiling cleaner in overalls wiping glass with a yellow sponge"></div>

  <div class="contact">
    <span class="contact__phone"><svg><use href="#icon-phone"/></svg>804-317-5286</span>
    <span class="contact__web">tallpinepowerwashing.com</span>
  </div>

  <div class="divider"></div>
  <div class="address-line" style="top:150px"></div>
  <div class="address-line" style="top:182px"></div>
  <div class="address-line" style="top:214px"></div>
  <div class="address-line" style="top:246px"></div>
</section>

<section class="postcard postcard--front">
  <div class="house-photo" role="img" aria-label="Photo of a large two-storey suburban house at dusk with lit windows, paver driveway and green lawn"></div>

  <div class="brand">
    <span class="brand__name">tallpine</span>
    <span class="brand__sub">power washing</span>
  </div>

  <div class="services">
    <p class="services__title">We Clean:-</p>
    <ul class="services__list">
      <li class="tile tile--houses"><svg><use href="#icon-house"/></svg>Houses</li>
      <li class="tile tile--decks"><svg><use href="#icon-deck"/></svg>Decks</li>
      <li class="tile tile--driveways"><svg><use href="#icon-car"/></svg>Driveways</li>
      <li class="tile tile--fences"><svg><use href="#icon-fence"/></svg>Fences</li>
    </ul>
  </div>

  <p class="offer">Mention this card and receive a <span class="offer__free">FREE</span> standard size Deck Wash</p>

  <div class="contact">
    <span class="contact__phone"><svg><use href="#icon-phone"/></svg>804-317-5286</span>
    <span class="contact__web">tallpinepowerwashing.com</span>
  </div>
</section>

</body>
</html>
```